"Warm Coat RBK" Business Card/Logo Design

I'm looking for a very creative look for my new business called "Warm Coat RBK" on a business card design. Don't be distracted by my "business card details" below....if you have other ideas on how you see "Warm Coat RBK" go for it. If probably should somehow give a look that I paint furniture....maybe a paint drip or something simple or you can get more creative....sky's the limit and I really need your creative eye on how to per tray that "Warm Coat RBK" means taking something old and turning into new again with some paint.

Industry/Entity Type

Business

Contact Information for Business Card

I refurbish and up-cycle furniture that needs "a little TLC'....thus, my business name was born called "Warm Coat RBK" (Those are my initials). I mainly paint old furniture of all styles and bring them back to life. I sometimes recreate furniture as well....I will make benches from old headboards of all sizes, etc. I'd love to see design that incorporate the crafty/creative side of me. If that means incorporating a paint brush, tools, paint cans, or furniture such as dressers, old vintage furniture, spindles, etc, etc. I don't know if something creative could be done with my initials (RBK). I really have a creative block of ideas and need your help bringing my "Warm Coat RBK" business to life.

P.S. Below is just one picture that I thought was neat and creative as they used a paintbrush but used spindles for the bristles and put their logo in the middle. Just an idea I thought was very unique and creative.

I'm very excited to see your design. Thank you for taking the time to create my logo/business card for me.

Rosa

Requirements
Must have
• Please include this information on the card:
• My Name: Rosa Kellerman
• Address: 48217 305th Ave NW, Birchwood Falls, NQ 55019
• E-Mail: warmcoatrbk@examplemail.net
• FB: http:/www.socialpage-sample.com/warmcoatrbk
• Cell: 555-014-2287

```html
<!DOCTYPE html>
<html lang="en">
<head>
<meta charset="utf-8">
<title>Warm Coat RBK – Business Card</title>
<link href="https://fonts.googleapis.com/css2?family=Montserrat:wght@400;600;800&display=swap" rel="stylesheet">
<style>
  :root {
    --backdrop: #ece8e3;
    --card: #ffffff;
    --ink: #2b2b2b;
    --brand-red: #b3202a;
    --mark-red: #c8232c;
    --faint: #f4e6e4;
  }
  * { box-sizing: border-box; margin: 0; padding: 0; }
  html, body {
    width: 1200px; height: 1000px; overflow: hidden;
    background: var(--backdrop);
    font-family: "Montserrat", Arial, sans-serif;
    color: var(--ink);
  }
  .canvas { position: relative; width: 1200px; height: 1000px; }
  .card {
    position: absolute; left: 265px; width: 666px; height: 397px;
    background: var(--card);
    box-shadow: 0 6px 14px rgba(0,0,0,.18);
  }
  .card--front { top: 73px; }
  .card--back { top: 532px; }

  .brand { position: absolute; display: flex; align-items: center; }
  .brand__square { background: var(--mark-red); flex: none; }
  .brand__name { font-weight: 800; color: var(--ink); line-height: 1.1; }

  .card--front .brand { left: 32px; top: 46px; gap: 24px; }
  .card--front .brand__square { width: 110px; height: 110px; }
  .card--front .brand__name { font-size: 42px; }

  .faint-square {
    position: absolute; left: 415px; top: 118px; width: 215px; height: 250px;
    background: var(--faint); opacity: .75;
  }

  .holder {
    position: absolute; left: 32px; top: 220px;
    font-size: 24px; font-weight: 600; color: var(--brand-red);
  }
  .contacts { position: absolute; left: 32px; top: 262px; list-style: none; }
  .contacts li {
    display: flex; align-items: center; gap: 6px;
    font-size: 17px; height: 27px;
  }
  .icon {
    width: 17px; height: 17px; background: var(--brand-red); border-radius: 2px;
    display: flex; align-items: center; justify-content: center; flex: none;
    color: #fff; font-size: 13px; font-weight: 600; line-height: 1;
  }
  .address { position: absolute; left: 32px; top: 350px; font-size: 17px; }

  .card--back .brand { left: 125px; top: 108px; gap: 38px; }
  .card--back .brand__square { width: 145px; height: 145px; }
  .card--back .brand__name { font-size: 56px; }
  .tagline {
    position: absolute; left: 0; right: 0; top: 347px; text-align: center;
    font-size: 18px; color: var(--brand-red);
  }
</style>
</head>
<body>
<main class="canvas">
  <section class="card card--front">
    <div class="faint-square" aria-hidden="true"></div>
    <div class="brand">
      <span class="brand__square" aria-hidden="true"></span>
      <span class="brand__name">Warm Coat<br>RBK</span>
    </div>
    <h1 class="holder">Rosa Kellerman</h1>
    <ul class="contacts">
      <li><span class="icon" aria-hidden="true"></span>warmcoatrbk</li>
      <li>
        <span class="icon" aria-hidden="true">
          <svg width="11" height="11" viewBox="0 0 24 24"><path fill="#fff" d="M6.6 10.8c1.4 2.8 3.8 5.1 6.6 6.6l2.2-2.2c.3-.3.7-.4 1-.2 1.1.4 2.3.6 3.6.6.6 0 1 .4 1 1V20c0 .6-.4 1-1 1C10.6 21 3 13.4 3 4c0-.6.4-1 1-1h3.5c.6 0 1 .4 1 1 0 1.3.2 2.5.6 3.6.1.3 0 .7-.2 1z"/></svg>
        </span>555-014-2287
      </li>
      <li><span class="icon" aria-hidden="true">@</span>warmcoatrbk@examplemail.net</li>
    </ul>
    <p class="address">48217 305th Ave NW, Birchwood Falls, NQ 55019</p>
  </section>

  <section class="card card--back">
    <div class="brand">
      <span class="brand__square" aria-hidden="true"></span>
      <span class="brand__name">Warm Coat<br>RBK</span>
    </div>
    <p class="tagline">Bring your furniture to life !</p>
  </section>
</main>
</body>
</html>
```